Halmi Rékas Physiotherapy Business Card Vienna

We need a business card design for a newly created Physiotherapy company based in Vienna Austria.
We seek a simple, modern, minimalist design without too much color variation. The font should look young/fresh, but definitely not childish or so. Since we are a starting Business, we currently haven't got a logo, if you feel like a logo would fit your design, feel free to use one, but it's not necessary.
Target Market(s)
Healthcare, young and elderly people with mobility issues
Industry/Entity Type
Health And Wellness
Contact Information for Business Card
Name: Réka Halmi
Title description: Physiotherapist
Phone num: +43 664 5290 4116
e-mail: reka.praxis@examplemail.net
Colors
Designer to choose colors to be used in the design.
Requirements
Must have
- Final design language must be in German, basically, the Title Description needs to be "Physiotherapeutin" the other details remain as in the English Language.
Nice to have
- Simple, modern, minimalist design
Should not have
- too many colors, Obvious use of a skeleton, skull, spline

```html
<!DOCTYPE html>
<html lang="de">
<head>
<meta charset="utf-8">
<title>Halmi Rékas Physiotherapy – Business Card</title>
<link rel="stylesheet" href="https://fonts.googleapis.com/css2?family=Open+Sans:wght@400;500&family=Tinos&display=swap">
<style>
  :root {
    --backdrop: #1c1c1d;
    --card: #141415;
    --card-edge: #202022;
    --ink: #e6e6e6;
    --ink-soft: #cfcfcf;
  }
  * { margin: 0; padding: 0; box-sizing: border-box; }
  html, body {
    width: 1200px;
    height: 900px;
    overflow: hidden;
    background: var(--backdrop);
  }
  .canvas {
    position: relative;
    width: 1200px;
    height: 900px;
    background: var(--backdrop);
  }
  .card {
    position: absolute;
    left: 290px;
    width: 620px;
    height: 355px;
    border-radius: 26px;
    background: var(--card);
    border: 1px solid var(--card-edge);
    box-shadow: 0 12px 30px rgba(0,0,0,0.45);
  }
  .card--front { top: 70px; }
  .card--back { top: 475px; }

  .brand {
    position: absolute;
    left: 0; right: 0;
    top: 128px;
    text-align: center;
    font-family: "Open Sans", sans-serif;
    font-weight: 400;
    color: var(--ink);
  }
  .brand__name {
    font-size: 38px;
    letter-spacing: 1px;
    line-height: 1;
  }
  .brand__field {
    margin-top: 8px;
    font-size: 12px;
    letter-spacing: 9px;
    padding-left: 9px;
  }

  .holder {
    position: absolute;
    left: 70px;
    top: 150px;
    color: var(--ink);
  }
  .holder__name {
    font-family: "Open Sans", sans-serif;
    font-size: 22px;
    font-weight: 400;
    letter-spacing: 0.5px;
    line-height: 1;
  }
  .holder__title {
    margin-top: 2px;
    font-family: "Tinos", serif;
    font-size: 15px;
    color: var(--ink-soft);
  }

  .contact {
    position: absolute;
    left: 300px;
    top: 186px;
    list-style: none;
    font-family: "Open Sans", sans-serif;
    font-size: 15px;
    color: var(--ink);
  }
  .contact__item {
    display: flex;
    align-items: center;
    gap: 12px;
    height: 24px;
    white-space: nowrap;
  }
  .contact__item + .contact__item { margin-top: 8px; }
  .contact__icon { width: 16px; height: 14px; flex: none; }
</style>
</head>
<body>
<main class="canvas">
  <section class="card card--front" aria-label="Card front">
    <div class="brand">
      <div class="brand__name">HALMI RÉKAS</div>
      <div class="brand__field">PHYSIOTHERAPY</div>
    </div>
  </section>

  <section class="card card--back" aria-label="Card back">
    <div class="holder">
      <div class="holder__name">RÉKA HALMI</div>
      <div class="holder__title">Physiotherapeutin</div>
    </div>
    <ul class="contact">
      <li class="contact__item">
        <svg class="contact__icon" viewBox="0 0 16 14" aria-hidden="true">
          <path d="M1 4.5 Q8 0 15 4.5 L13.5 6.5 L11 5.5 L11 4 Q8 3 5 4 L5 5.5 L2.5 6.5 Z" fill="#e6e6e6"/>
          <rect x="3" y="7" width="10" height="6" rx="1" fill="#e6e6e6"/>
          <circle cx="8" cy="10" r="1.6" fill="#141415"/>
        </svg>
        <span>+43 664 5290 4116</span>
      </li>
      <li class="contact__item">
        <svg class="contact__icon" viewBox="0 0 16 14" aria-hidden="true">
          <rect x="1" y="2" width="14" height="10" rx="1" fill="#e6e6e6"/>
          <path d="M1.5 2.8 L8 8 L14.5 2.8" fill="none" stroke="#141415" stroke-width="1.3"/>
        </svg>
        <span>reka.praxis@examplemail.net</span>
      </li>
    </ul>
  </section>
</main>
</body>
</html>
```